Tidecrest NZ Brand, Revenue, Promotions & Events

I need an innovative business card that pops my brand. I like the colours against darker gradients and i'm not afraid to be bold.

I run my own Business, Brand, Event & Promotion company. I specialise in breathing life into businesses and adding atmosphere to promotions and events. I am concept based lady that likes to test the boundaries and create stand out campaigns that connect with the consumer.

I have 12 years business experience in a realm of interesting fields form 11 years in coordinating international music festivals & promotions, 6 years in radio with 8 radio awards including a NZ radio award for best sales team in NZ and was the national brand and sales manager for New Zealands 1st indoor entertainment mall. With 10 years of experience in advertising sales, I have an eye for creating revenue streams for businesses and thrive on implementing campaigns that compliment those streams.

I love sayings like "Do what you love, love what you do" and believe that you can achieve anything you want.

I have been fortunate in my career that my connections have carried me without needing to promote my business however it is important that I start to do so.

Target Market(s)

Decision makers 25 to 54

Contact Information for Business Card

Petra Ollingham
Director
p. 022 587 3091
e. petra@tidecrest.nz
www.tidecrest.nz

FB, IG and Linkedin logo

Font styles to use
Sans Serif

Colors

Designer to choose colors to be used in the design.

Requirements
Must have
• Petra Ollingham
• Director
• p. 022 587 3091
• e. petra@tidecrest.nz
• www.tidecrest.nz
• FB, IG and Linkedin logo
Nice to have
• I am looking for a business card with character, that leaves my presence with my customer and makes them remember my brand & optimistic personality when i walk out the door.

```html
<!DOCTYPE html>
<html lang="en">
<head>
<meta charset="utf-8">
<title>Tidecrest NZ – Business Card</title>
<link rel="stylesheet" href="https://fonts.googleapis.com/css2?family=Lato:ital,wght@0,400;0,700;0,900;1,400&display=swap">
<style>
  :root {
    --brand-blue: #29abe2;
    --ink: #2b2b2b;
    --muted-grey: #8a8a8a;
    --block-grey: #b5b5b5;
    --paper: #ffffff;
    --backdrop: #1f1f1f;
  }
  * { margin: 0; padding: 0; box-sizing: border-box; }
  html, body {
    width: 1200px; height: 878px; overflow: hidden;
    background: var(--backdrop);
    font-family: "Lato", sans-serif;
  }
  .stage { position: relative; width: 1200px; height: 878px; }
  .card {
    position: absolute; left: 290px; width: 620px; height: 354px;
    overflow: hidden;
  }
  .card--front { top: 64px; background: var(--brand-blue); color: var(--paper); }
  .card--back { top: 460px; background: var(--paper); color: var(--ink); }

  .front-brand {
    position: absolute; left: 0; right: 0; top: 128px; text-align: center;
  }
  .front-brand .wordmark {
    font-weight: 700; font-size: 50px; letter-spacing: 4px; line-height: 1;
  }
  .front-brand .tagline {
    margin-top: 10px; font-size: 15px; letter-spacing: 1px;
  }

  .back-brand { position: absolute; left: 40px; top: 34px; }
  .back-brand .wordmark {
    color: var(--brand-blue); font-weight: 700; font-size: 38px;
    letter-spacing: 3px; line-height: 1;
  }
  .back-brand .tagline {
    margin-top: 6px; color: var(--muted-grey); font-size: 12.5px; letter-spacing: 0.6px;
  }

  .address {
    position: absolute; left: 44px; top: 150px;
    font-size: 18px; line-height: 24px; color: var(--ink);
  }
  .contact-list {
    position: absolute; left: 40px; top: 212px; list-style: none;
    font-size: 18px; color: var(--ink);
  }
  .contact-list li { display: flex; align-items: center; height: 27px; }
  .contact-list svg { width: 18px; height: 18px; margin-right: 12px; }

  .person {
    position: absolute; right: 44px; top: 214px; text-align: right;
  }
  .person .name {
    color: var(--brand-blue); font-weight: 900; font-size: 33px; line-height: 1;
  }
  .person .role { margin-top: 6px; font-size: 19px; color: var(--ink); }

  .follow {
    position: absolute; right: 44px; top: 300px;
    display: flex; align-items: center; gap: 10px;
  }
  .follow .label {
    color: var(--brand-blue); font-size: 18px; letter-spacing: 0.5px; margin-right: 12px;
  }
  .social-square {
    width: 20px; height: 20px; border-radius: 4px; background: var(--brand-blue);
  }

  .base-band {
    position: absolute; left: 0; right: 0; bottom: 0; height: 14px;
    background: var(--brand-blue);
  }
  .base-block {
    position: absolute; left: 0; bottom: 0; width: 44px; height: 18px;
    background: var(--block-grey); border-right: 6px solid var(--paper);
  }
</style>
</head>
<body>
<main class="stage">
  <section class="card card--front" aria-label="Card front">
    <div class="front-brand">
      <div class="wordmark">TIDECREST NZ</div>
      <div class="tagline">BRAND | REVENUE | EVENTS &amp; PROMOTIONS</div>
    </div>
  </section>

  <section class="card card--back" aria-label="Card back">
    <div class="back-brand">
      <div class="wordmark">TIDECREST NZ</div>
      <div class="tagline">BRAND | REVENUE | EVENTS &amp; PROMOTIONS</div>
    </div>

    <p class="address">1234 First Line Address<br>5678 Second Line Address</p>

    <ul class="contact-list">
      <li>
        <svg viewBox="0 0 24 24" aria-hidden="true"><path fill="var(--brand-blue)" d="M6.6 10.8a15 15 0 0 0 6.6 6.6l2.2-2.2c.3-.3.7-.4 1-.2 1.1.4 2.3.6 3.6.6.6 0 1 .4 1 1V20c0 .6-.4 1-1 1A17 17 0 0 1 3 4c0-.6.4-1 1-1h3.5c.6 0 1 .4 1 1 0 1.3.2 2.5.6 3.6.1.3 0 .7-.2 1z"/></svg>
        022 587 3091
      </li>
      <li>
        <svg viewBox="0 0 24 24" aria-hidden="true"><rect x="2" y="5" width="20" height="14" rx="1" fill="var(--brand-blue)"/><path d="M2.5 5.5 12 13l9.5-7.5" fill="none" stroke="#fff" stroke-width="1.6"/></svg>
        petra@tidecrest.nz
      </li>
      <li>
        <svg viewBox="0 0 24 24" aria-hidden="true"><g fill="none" stroke="var(--brand-blue)" stroke-width="1.8"><circle cx="12" cy="12" r="9.5"/><ellipse cx="12" cy="12" rx="4" ry="9.5"/><path d="M2.5 12h19M4 7h16M4 17h16"/></g></svg>
        www.tidecrest.nz
      </li>
    </ul>

    <div class="person">
      <div class="name">Petra Ollingham</div>
      <div class="role">Director</div>
    </div>

    <div class="follow">
      <span class="label">FOLLOW US</span>
      <span class="social-square" role="img" aria-label="Social profile link"></span>
      <span class="social-square" role="img" aria-label="Social profile link"></span>
      <span class="social-square" role="img" aria-label="Social profile link"></span>
    </div>

    <div class="base-band"></div>
    <div class="base-block"></div>
  </section>
</main>
</body>
</html>
```